I need a business card to launch my business. I am a carpenter who works with wood and metal framing. I do commercial and residential properties. I do the final fixtures in expensive residential properties. For example custom made wardrobes, prefinished doors and skirtings. I have an eye for detail and take pride in my work.

I don't want to be pigeon holed as a guy with a tool belt and a hammer. I want to look like a professional company. I want my logo to be modern and young and edgy. I don't have any preference for colours but don't want yellow.

Industry/Entity Type

Residential

Contact Information for Business Card

Oakridge Joinery
specialising in residential and commercial fit outs

Mark Dawson
Phone: 0417 352 068
oakridgejoinery@mailbox-example.com

Logo styles of interest
Pictorial/Combination Logo
Wordmark Logo
Lettermark Logo

```html
<!DOCTYPE html>
<html lang="en">
<head>
<meta charset="utf-8">
<title>Oakridge Joinery – Business Card</title>
<link rel="stylesheet" href="https://fonts.googleapis.com/css2?family=Lato:wght@300;700;900&display=swap">
<style>
  :root {
    --wood-light: #e3a45e;
    --wood-mid: #cc7f36;
    --wood-deep: #a95b24;
    --ink: #2b2a28;
    --cream: #f8eddf;
    --rule: rgba(248, 237, 223, 0.75);
  }
  html, body {
    margin: 0;
    padding: 0;
    width: 1200px;
    height: 693px;
    overflow: hidden;
    background: var(--wood-mid);
  }
  .card {
    position: relative;
    width: 1200px;
    height: 693px;
    overflow: hidden;
    font-family: "Lato", sans-serif;
  }
  .card__backdrop {
    position: absolute;
    inset: 0;
    background:
      linear-gradient(90deg, rgba(120, 55, 15, 0.18) 0%, rgba(255, 210, 150, 0.12) 35%, rgba(120, 55, 15, 0.12) 65%, rgba(255, 210, 150, 0.1) 100%),
      linear-gradient(160deg, var(--wood-light) 0%, var(--wood-mid) 50%, var(--wood-deep) 100%);
  }
  .tagline {
    position: absolute;
    left: 167px;
    top: 187px;
    margin: 0;
    font-weight: 300;
    font-size: 31.5px;
    letter-spacing: 0.4px;
    color: var(--cream);
    white-space: nowrap;
  }
  .wordmark {
    position: absolute;
    left: 0;
    top: 0;
    width: 1200px;
    height: 693px;
  }
  .wordmark__name {
    font-family: "Lato", sans-serif;
    font-weight: 700;
    fill: var(--ink);
  }
  .wordmark__rule {
    stroke: var(--rule);
    stroke-width: 1.2;
  }
  .contact {
    position: absolute;
    left: 303px;
    top: 470px;
    margin: 0;
    font-weight: 700;
    font-size: 33.5px;
    line-height: 37px;
    color: var(--ink);
    letter-spacing: 0.2px;
    white-space: nowrap;
  }
  .contact span { display: block; }
</style>
</head>
<body>
  <main class="card">
    <div class="card__backdrop" role="img" aria-label="Warm orange timber panelling with vertical and horizontal boards"></div>

    <p class="tagline">Specialising in residential and commercial fit outs</p>

    <svg class="wordmark" viewBox="0 0 1200 693" aria-label="Oakridge Joinery">
      <line class="wordmark__rule" x1="167" y1="231" x2="1039" y2="231"/>
      <text class="wordmark__name" x="167" y="389" font-size="182" textLength="872" lengthAdjust="spacingAndGlyphs">OAKRIDGE</text>
      <text class="wordmark__name" x="169" y="442" font-size="56" textLength="873" lengthAdjust="spacing">JOINERY</text>
      <line class="wordmark__rule" x1="167" y1="460" x2="1039" y2="460"/>
    </svg>

    <p class="contact">
      <span class="contact__phone">Call Mark Dawson on 0417 352 068</span>
      <span class="contact__email">oakridgejoinery@mailbox-example.com</span>
    </p>
  </main>
</body>
</html>
```